Restaurant service company needs a website!

I am looking for a skilled web designer/developer to create a professional, responsive, and easy-to-navigate website for my company, which specializes in servicing restaurant cooking equipment. The site should communicate trust, reliability, and technical expertise to our target audience, restaurant owners, managers, and commercial kitchen operators. I have included the company logos, if any other format for them is needed please let me know.

Target Market(s)

restaurant owners, managers, and commercial kitchen operators

Industry/Entity Type

Commercial Kitchen Equipment Service

Coding

Coded - Design and coding required

Number of Pages Required

1 page

Font styles to use
Serif
Sans Serif

Requirements
Must have
• Contact and service request forms, Click-to-call functionality for mobile, Clean, modern layout with strong visuals, Easy navigation, mobile-friendly
Nice to have
• Testimonials or Reviews, If possible a click-to-text functionality for mobile.
Should not have
• Any mention of Refrigeration or HVAC, "Free Quotes"

```html
<!DOCTYPE html>
<html lang="en">
<head>
<meta charset="utf-8">
<title>Ironpath Restaurant Service</title>
<link rel="stylesheet" href="https://fonts.googleapis.com/css2?family=Josefin+Sans:wght@600;700&family=Montserrat:wght@400;500;600;700&display=swap">
<style>
:root{
  --teal:#13647a;
  --teal-dark:#0f4f61;
  --teal-deep:#0c4252;
  --teal-soft:#1d7289;
  --orange:#ef8c0a;
  --grey:#f3f3f3;
  --ink:#2b2b2b;
  --white:#fff;
}
*{margin:0;padding:0;box-sizing:border-box}
html,body{width:1200px;height:4979px;overflow:hidden;background:var(--white)}
body{font-family:"Montserrat",sans-serif;color:var(--ink)}
.page{position:relative;width:1200px;height:4979px;overflow:hidden}
.abs{position:absolute}
.head{font-family:"Josefin Sans",sans-serif;font-weight:700;text-transform:uppercase;color:var(--teal);letter-spacing:.5px}
.btn{position:absolute;display:flex;align-items:center;justify-content:center;gap:6px;font-size:13px;font-weight:700;text-transform:uppercase;color:var(--white);text-decoration:none;letter-spacing:.3px}
.btn-orange{background:var(--orange);border-radius:3px}
.btn-dark{background:var(--teal-dark);border-radius:4px}
.btn-pill{background:var(--orange);border-radius:26px}
.photo{position:absolute}

/* top bar & nav */
.topbar{left:590px;top:0;width:610px;height:38px;background:var(--teal);clip-path:polygon(20px 0,100% 0,100% 100%,0 100%);color:var(--white);font-size:14px;display:flex;align-items:center;gap:36px;padding-left:50px}
.topbar span{display:flex;align-items:center;gap:10px}
.logo-text{left:116px;top:30px;display:flex;align-items:center;gap:12px;font-family:"Josefin Sans",sans-serif;font-weight:700;font-size:26px;color:var(--teal)}
.logo-square{width:26px;height:26px;border:3px solid var(--teal)}
.nav{left:455px;top:62px;display:flex;gap:0}
.nav a{position:absolute;top:0;font-size:13px;font-weight:600;color:var(--teal-dark);text-decoration:none;white-space:nowrap}
.nav a.active::after{content:"";position:absolute;left:0;right:0;top:24px;height:2px;background:var(--teal)}

/* hero */
.hero{left:0;top:106px;width:1200px;height:657px;border-radius:0 0 60px 60px;overflow:hidden;background:linear-gradient(90deg,#0e5d72 0%,#14697f 45%,#2a7d91 100%)}
.hero-photo{left:520px;top:0;width:680px;height:657px;background:radial-gradient(ellipse at 55% 45%,#2e4b55 0%,#1b6277 45%,rgba(20,105,127,0) 75%)}
.hero-label{left:112px;top:274px;font-size:13px;font-weight:700;color:var(--white);letter-spacing:1px}
.hero-title{left:112px;top:300px;font-size:43px;line-height:47px;color:var(--white)}
.btn-outline{border:1.5px solid var(--white);border-radius:2px}

/* about */
.about-photo{left:116px;top:880px;width:431px;height:430px;border-radius:40px;background:linear-gradient(135deg,#3a4c66,#6d7a8c 55%,#b9a24c)}
.about-title{left:611px;top:893px;font-size:40px}
.about-sub{left:611px;top:938px;font-size:26px;display:flex;align-items:center;gap:12px}
.about-sub::after{content:"";width:38px;height:3px;background:var(--teal)}
.about-text{left:611px;top:983px;width:475px;font-size:17px;line-height:27px;color:#333}
.about-quote{left:611px;top:1123px;width:480px;padding-left:14px;border-left:2px solid var(--teal);font-size:17px;line-height:27px;color:#333}
.divider{left:0;top:1395px;width:1200px;height:1px;background:#e7e7e7}

/* services */
.section-title{width:1200px;left:0;text-align:center;font-size:40px}
.underline-c{left:562px;width:76px;height:3px;background:var(--teal)}
.card{position:absolute;top:1572px;width:294px;height:318px;overflow:hidden}
.card .shade{position:absolute;inset:0;background:linear-gradient(180deg,rgba(0,0,0,0) 45%,rgba(0,0,0,.65))}
.card h3{position:absolute;left:0;right:0;bottom:22px;text-align:center;color:var(--white);font-family:"Josefin Sans",sans-serif;font-size:22px;line-height:24px;text-transform:uppercase}
.card-active{position:absolute;left:302px;top:1546px;width:295px;height:374px;background:var(--teal);border-radius:6px;color:var(--white);text-align:center;padding:88px 22px 0}
.card-active h3{font-family:"Josefin Sans",sans-serif;font-size:22px;line-height:26px;text-transform:uppercase;margin-bottom:12px}
.card-active p{font-size:14px;line-height:21px}
.card-active .mini{display:inline-flex;margin-top:16px;border:1.5px solid var(--white);padding:10px 26px;font-size:12px;font-weight:700;border-radius:2px}

/* why */
.why{left:0;top:1890px;width:1200px;height:677px;background:var(--grey)}
.why-title{left:130px;top:2038px;font-size:34px;line-height:43px}
.why-line{left:130px;top:2130px;width:117px;height:3px;background:var(--teal)}
.why-item{position:absolute;left:130px;display:flex;gap:22px}
.tick{width:32px;height:32px;border-radius:50%;background:var(--teal);display:flex;align-items:center;justify-content:center;flex:none;margin-top:4px}
.why-item h4{font-size:17px;font-weight:700;color:var(--teal);text-transform:uppercase;margin-bottom:4px}
.why-item p{font-size:13px;color:#444}

/* cta */
.cta{left:68px;top:2664px;width:1090px;height:506px;border-radius:14px;overflow:hidden;background:linear-gradient(90deg,#3c3a34 0%,#1e2a33 40%,#1b2730 60%,#3d3d3a 100%)}
.cta-vline{left:636px;top:2615px;width:2px;height:66px;background:var(--teal)}
.cta-title{left:68px;width:1090px;top:2806px;text-align:center;color:var(--white);font-size:35px;line-height:42px}
.cta-text{left:310px;width:606px;top:2898px;text-align:center;color:#eee;font-size:14px;line-height:26px}

/* reviews */
.rev-label{left:0;width:1240px;top:3267px;text-align:center;font-size:14px;letter-spacing:.5px;color:#333}
.rev-photo-a{left:107px;top:3365px;width:265px;height:305px;border-radius:16px;background:linear-gradient(135deg,#2a2c2f,#6b6f73 60%,#c9c5ba)}
.rev-photo-b{left:260px;top:3487px;width:248px;height:283px;border-radius:16px;border:6px solid var(--white);background:linear-gradient(135deg,#cfcbc4,#9a9691 50%,#e8e4dd)}
.rev-text{left:570px;top:3470px;width:560px;font-size:21px;line-height:31px;color:#333}
.rev-name{left:564px;top:3636px;font-size:21px;font-weight:700;color:#222}
.stars{left:568px;top:3672px;color:var(--orange);font-size:22px;letter-spacing:2px}
.arrow{position:absolute;top:3717px;width:38px;height:38px;border-radius:50%;background:var(--teal);display:flex;align-items:center;justify-content:center}

/* contact */
.contact{left:0;top:3901px;width:1200px;height:760px;background:linear-gradient(180deg,#206f85,#1a6b81 60%,#1b6c82)}
.contact-eyebrow{left:132px;top:4010px;font-size:16px;color:var(--white)}
.contact-title{left:132px;top:4040px;font-size:40px;color:var(--white)}
.contact-text{left:134px;top:4113px;width:420px;font-size:15px;line-height:25px;color:var(--white)}
.c-item{position:absolute;left:130px;display:flex;gap:16px;align-items:center;color:var(--white);font-size:16px;line-height:19px}
.c-icon{width:36px;height:36px;border-radius:50%;background:var(--white);display:flex;align-items:center;justify-content:center;flex:none}
.form{left:615px;top:3969px;width:475px;height:448px;background:#145a6d;border-radius:14px}
.form-title{left:684px;top:4006px;font-size:24px;color:var(--white);letter-spacing:1px}
.field{position:absolute;background:var(--white);font-size:13px;color:#333;padding:14px 22px}

/* footer */
.footer{left:0;top:4562px;width:1200px;height:417px;background:var(--white);border-radius:60px 60px 0 0}
.f-logo{left:100px;top:4610px;width:225px;text-align:center;font-family:"Josefin Sans",sans-serif;font-weight:700;color:var(--teal)}
.f-square{width:84px;height:84px;border:5px solid var(--teal);margin:0 auto 18px}
.f-name{font-size:24px;line-height:26px;white-space:nowrap}
.f-tag{font-size:11px;line-height:14px;letter-spacing:2.5px;white-space:nowrap}
.social{left:156px;top:4790px;display:flex;gap:8px}
.social span{width:30px;height:30px;border-radius:50%;background:var(--teal)}
.f-col{position:absolute;top:4602px}
.f-col h5{font-family:"Josefin Sans",sans-serif;font-size:19px;color:var(--teal);text-transform:uppercase;padding-bottom:8px;border-bottom:2px solid #d9e4e8;width:166px;margin-bottom:16px}
.f-col li{list-style:none;font-size:13px;line-height:24px;color:#333}
.f-contact{display:flex;gap:12px;align-items:center;font-size:12px;line-height:16px;color:#333;margin-bottom:20px}
.f-contact .c-icon{background:var(--teal);width:34px;height:34px}
.f-rule{left:108px;top:4908px;width:990px;height:1px;background:#ddd}
.copy{left:0;width:1200px;top:4930px;text-align:center;font-size:13px;color:#333}
</style>
</head>
<body>
<div class="page">

  <!-- header -->
  <div class="abs topbar">
    <span><svg width="18" height="13" viewBox="0 0 18 13"><rect x="1" y="1" width="16" height="11" fill="none" stroke="#fff" stroke-width="1.5"/><path d="M1 1l8 6 8-6" fill="none" stroke="#fff" stroke-width="1.5"/></svg>enquiry@ironpath-service.com</span>
    <span><svg width="16" height="16" viewBox="0 0 24 24"><path d="M6.6 10.8a15 15 0 006.6 6.6l2.2-2.2a1 1 0 011-.25 11 11 0 003.6.6 1 1 0 011 1V20a1 1 0 01-1 1A17 17 0 013 4a1 1 0 011-1h3.5a1 1 0 011 1 11 11 0 00.6 3.6 1 1 0 01-.25 1z" fill="#fff"/></svg>Phone Number <b>(+123) 456 7890</b></span>
  </div>
  <div class="abs logo-text"><span class="logo-square"></span>IRONPATH</div>
  <nav class="abs nav">
    <a class="active" href="#" style="left:0">HOME</a>
    <a href="#" style="left:91px">ABOUT US</a>
    <a href="#" style="left:213px">SERVICES</a>
    <a href="#" style="left:330px">WHY US</a>
    <a href="#" style="left:432px">REVIEWS</a>
    <a href="#" style="left:547px">CONTACT US</a>
  </nav>

  <!-- hero -->
  <section class="abs hero">
    <div class="photo hero-photo" role="img" aria-label="Technician's hands servicing a commercial gas range cooktop"></div>
  </section>
  <div class="abs hero-label">IRONPATH RESTAURANT SERVICE</div>
  <h1 class="abs head hero-title" style="color:#fff">Fast &amp; Reliable<br>Commercial Kitchen<br>Equipment Service</h1>
  <a class="btn btn-outline" href="#" style="left:112px;top:463px;width:182px;height:43px">Request Service ›</a>
  <a class="btn btn-orange" href="tel:+11234567890" style="left:302px;top:463px;width:181px;height:43px"><svg width="13" height="13" viewBox="0 0 24 24"><path d="M6.6 10.8a15 15 0 006.6 6.6l2.2-2.2a1 1 0 011-.25 11 11 0 003.6.6 1 1 0 011 1V20a1 1 0 01-1 1A17 17 0 013 4a1 1 0 011-1h3.5a1 1 0 011 1 11 11 0 00.6 3.6 1 1 0 01-.25 1z" fill="#fff"/></svg>Call Us Now</a>

  <!-- about -->
  <div class="photo about-photo" role="img" aria-label="Gloved technician repairing internal components of kitchen equipment"></div>
  <h2 class="abs head about-title">About Ironpath</h2>
  <div class="abs head about-sub">Restaurant Service</div>
  <p class="abs about-text">Lorem ipsum dolor sit amet, consectetur adipiscing elit, sed do eiusmod tempor incididunt ut labore et dolore magna aliqua. Quis ipsum suspendisse ultrices gravida. Risus commodo viverra</p>
  <p class="abs about-quote">Lorem ipsum dolor sit amet, consectetur adipiscing elit, sed do eiusmod tempor incididunt ut labore et dolore magna aliqua ipsum suspendisse</p>
  <a class="btn btn-dark" href="#" style="left:611px;top:1235px;width:221px;height:51px">Request Service ›</a>
  <div class="abs divider"></div>

  <!-- services -->
  <h2 class="abs head section-title" style="top:1450px">Service Provide</h2>
  <div class="abs underline-c" style="top:1496px"></div>
  <div class="card" style="left:0"><div class="photo" style="inset:0;background:linear-gradient(135deg,#4b4f55,#9aa2a8 50%,#3a3d42)" role="img" aria-label="Technician performing maintenance on a range burner"></div><div class="shade"></div><h3>Preventive<br>Maintenance</h3></div>
  <div class="card" style="left:604px"><div class="photo" style="inset:0;background:linear-gradient(135deg,#c9b9a6,#4a4a4d 50%,#2f5c9c)" role="img" aria-label="Smiling technician servicing a commercial oven"></div><div class="shade"></div><h3>Emergency<br>Servicing</h3></div>
  <div class="card" style="left:907px"><div class="photo" style="inset:0;background:linear-gradient(135deg,#3a3a3c,#8b8e90 55%,#2d2e30)" role="img" aria-label="Technician installing commercial kitchen equipment"></div><div class="shade"></div><h3>Installation<br>Service</h3></div>
  <div class="card-active">
    <h3>Cooking<br>Equipment Repair</h3>
    <p>Lorem ipsum dolor sit amet, consectetur adipiscing elit, sed do eiusmod tempor incididunt ut labore et dolore magna</p>
    <span class="mini">REQUEST SERVICE ›</span>
  </div>

  <!-- why -->
  <section class="abs why"></section>
  <h2 class="abs head why-title">Why Choose Us For You<br>Restaurant Service</h2>
  <div class="abs why-line"></div>
  <div class="why-item" style="top:2172px"><span class="tick"><svg width="14" height="11" viewBox="0 0 14 11"><path d="M1 5.5l4 4L13 1" fill="none" stroke="#fff" stroke-width="2.4"/></svg></span><div><h4>Fast Response Times</h4><p>Lorem ipsum dolor sit amet, consectetur adipiscing</p></div></div>
  <div class="why-item" style="top:2244px"><span class="tick"><svg width="14" height="11" viewBox="0 0 14 11"><path d="M1 5.5l4 4L13 1" fill="none" stroke="#fff" stroke-width="2.4"/></svg></span><div><h4>Reliable Service</h4><p>Lorem ipsum dolor sit amet, consectetur adipi</p></div></div>
  <div class="why-item" style="top:2322px"><span class="tick"><svg width="14" height="11" viewBox="0 0 14 11"><path d="M1 5.5l4 4L13 1" fill="none" stroke="#fff" stroke-width="2.4"/></svg></span><div><h4>Certified Technicians</h4><p>Lorem ipsum dolor sit amet, consectetur adipi</p></div></div>
  <a class="btn btn-orange" href="#" style="left:130px;top:2403px;width:194px;height:45px">Request Service ›</a>
  <svg class="abs" style="left:620px;top:1950px" width="560" height="560" viewBox="0 0 560 560">
    <path d="M345 22 A255 255 0 1 0 405 500" fill="none" stroke="#13647a" stroke-width="30"/>
  </svg>
  <div class="photo" style="left:682px;top:2005px;width:444px;height:444px;border-radius:50%;background:linear-gradient(135deg,#5a4a3e,#9b8b7a 40%,#3d6f9e 75%,#2d2d30)" role="img" aria-label="Technician adjusting a built-in commercial oven"></div>
  <div class="photo" style="left:610px;top:2210px;width:270px;height:270px;border-radius:50%;border:6px solid #fff;background:linear-gradient(135deg,#2b2c2e,#6d7174 55%,#c7c2b6)" role="img" aria-label="Hands using a wrench on an oven fitting"></div>

  <!-- cta -->
  <div class="abs cta-vline"></div>
  <div class="photo cta" role="img" aria-label="Technicians at work on commercial kitchen equipment, darkened"></div>
  <svg class="abs" style="left:610px;top:2742px" width="48" height="48" viewBox="0 0 48 48"><rect x="10" y="10" width="28" height="28" fill="none" stroke="#fff" stroke-width="2"/></svg>
  <h2 class="abs head cta-title">Cooking Equipment Can't Wait.<br>Request Service Now!</h2>
  <p class="abs cta-text">Lorem ipsum dolor sit amet, consectetur adipiscing elit, sed do eiusmod tempor incididunt ut labore et dolore magna aliqua. Quis ipsum suspendisse ultrices</p>
  <a class="btn btn-pill" href="#" style="left:527px;top:2990px;width:210px;height:50px">Request Service ›</a>

  <!-- reviews -->
  <div class="abs rev-label">CUSTOMER REVIEWS</div>
  <h2 class="abs head section-title" style="top:3296px;font-size:36px;left:20px">What Customer Says</h2>
  <div class="abs underline-c" style="top:3340px;left:534px;width:172px;height:2px"></div>
  <div class="photo rev-photo-a" role="img" aria-label="Hand cleaning a commercial grill grate"></div>
  <div class="photo rev-photo-b" role="img" aria-label="Stainless steel commercial combi oven"></div>
  <svg class="abs" style="left:570px;top:3415px" width="52" height="40" viewBox="0 0 52 40"><path d="M2 38V22C2 10 9 3 20 1v7c-6 2-9 6-9 12h9v18zM30 38V22C30 10 37 3 48 1v7c-6 2-9 6-9 12h9v18z" fill="#13647a"/></svg>
  <p class="abs rev-text">Lorem ipsum dolor sit amet, consectetur adipiscing elit, sed do eiusmod tempor incididunt ut labore et dolore magna aliqua. Quis ipsum suspendisse ultrices gravida. Risus commodo viverra maecenas</p>
  <div class="abs rev-name">Daniel Mercer</div>
  <div class="abs stars">★★★★★</div>
  <span class="arrow" style="left:577px"><svg width="16" height="12" viewBox="0 0 16 12"><path d="M15 6H2M6 1L1 6l5 5" fill="none" stroke="#fff" stroke-width="1.8"/></svg></span>
  <span class="arrow" style="left:631px"><svg width="16" height="12" viewBox="0 0 16 12"><path d="M1 6h13M10 1l5 5-5 5" fill="none" stroke="#fff" stroke-width="1.8"/></svg></span>

  <!-- contact -->
  <section class="abs contact" role="img" aria-label="Commercial kitchen backdrop in teal tint"></section>
  <div class="abs contact-eyebrow">GET IN TOUCH</div>
  <h2 class="abs head contact-title">Contact Us</h2>
  <p class="abs contact-text">Call, Text or Email to book a consultation and get your free energy saving request.</p>
  <div class="c-item" style="top:4195px"><span class="c-icon"><svg width="14" height="18" viewBox="0 0 14 18"><path d="M7 0a7 7 0 017 7c0 5-7 11-7 11S0 12 0 7a7 7 0 017-7z" fill="#1a6b81"/><circle cx="7" cy="7" r="2.6" fill="#fff"/></svg></span><span>2480 Harbor View Rd.,<br>Bayside, FL 33000</span></div>
  <div class="c-item" style="top:4265px"><span class="c-icon"><svg width="16" height="16" viewBox="0 0 24 24"><path d="M6.6 10.8a15 15 0 006.6 6.6l2.2-2.2a1 1 0 011-.25 11 11 0 003.6.6 1 1 0 011 1V20a1 1 0 01-1 1A17 17 0 013 4a1 1 0 011-1h3.5a1 1 0 011 1 11 11 0 00.6 3.6 1 1 0 01-.25 1z" fill="#1a6b81"/></svg></span><span>Phone Number<br>+123 456 7890</span></div>
  <div class="c-item" style="top:4335px"><span class="c-icon"><svg width="18" height="13" viewBox="0 0 18 13"><rect x="1" y="1" width="16" height="11" fill="none" stroke="#1a6b81" stroke-width="1.6"/><path d="M1 1l8 6 8-6" fill="none" stroke="#1a6b81" stroke-width="1.6"/></svg></span><span>Email address<br>info@ironpath-service.com</span></div>

  <form class="abs form" action="#"></form>
  <h3 class="abs head form-title" style="color:#fff">Request &nbsp;A Service</h3>
  <div class="field" style="left:676px;top:4055px;width:181px;height:43px">First Name</div>
  <div class="field" style="left:861px;top:4055px;width:185px;height:43px">Last Name</div>
  <div class="field" style="left:676px;top:4110px;width:370px;height:43px">Email address</div>
  <div class="field" style="left:676px;top:4166px;width:370px;height:43px">Phone Number</div>
  <div class="field" style="left:676px;top:4221px;width:370px;height:85px">Leave Message</div>
  <a class="btn btn-pill" href="#" style="left:675px;top:4322px;width:201px;height:50px">Send Message ›</a>

  <!-- footer -->
  <footer class="abs footer"></footer>
  <div class="abs f-logo"><div class="f-square"></div><div class="f-name">IRONPATH</div><div class="f-tag">RESTAURANT SERVICE</div></div>
  <div class="abs social"><span></span><span></span><span></span></div>
  <div class="f-col" style="left:400px">
    <h5>Contact Us</h5>
    <div class="f-contact"><span class="c-icon"><svg width="14" height="18" viewBox="0 0 14 18"><path d="M7 0a7 7 0 017 7c0 5-7 11-7 11S0 12 0 7a7 7 0 017-7z" fill="#fff"/><circle cx="7" cy="7" r="2.6" fill="#13647a"/></svg></span><span>2480 Harbor View Rd.,<br>Bayside, FL 33000</span></div>
    <div class="f-contact"><span class="c-icon"><svg width="15" height="15" viewBox="0 0 24 24"><path d="M6.6 10.8a15 15 0 006.6 6.6l2.2-2.2a1 1 0 011-.25 11 11 0 003.6.6 1 1 0 011 1V20a1 1 0 01-1 1A17 17 0 013 4a1 1 0 011-1h3.5a1 1 0 011 1 11 11 0 00.6 3.6 1 1 0 01-.25 1z" fill="#fff"/></svg></span><span>+1 555-010-2647</span></div>
    <div class="f-contact"><span class="c-icon"><svg width="16" height="12" viewBox="0 0 18 13"><rect x="1" y="1" width="16" height="11" fill="none" stroke="#fff" stroke-width="1.6"/><path d="M1 1l8 6 8-6" fill="none" stroke="#fff" stroke-width="1.6"/></svg></span><span>enquiry@ironpath-service.com</span></div>
  </div>
  <div class="f-col" style="left:680px">
    <h5>Navigation</h5>
    <ul><li>Home</li><li>About Us</li><li>Services</li><li>Why Us</li><li>Reviews</li></ul>
  </div>
  <div class="f-col" style="left:900px">
    <h5>Resources</h5>
    <ul><li>Privacy Policy</li><li>Terms of Use</li><li>Support</li><li>Contact Us</li></ul>
  </div>
  <div class="abs f-rule"></div>
  <div class="abs copy">Copyright © 2025 IRONPATH. All Right Reserved</div>

</div>
</body>
</html>
```